professional business card

A Clean looking business card for a money transfer company. Our company is call Velorix= Transfer + Send = Transcend (next level)
to show professionalism as well as some effects to show digital tech.

1 side to have position, name and address
2 side to have company name and show that we provide money exchange and cross-border money transfer

Target Market(s)

Remittance companies and high net worth individuals

Industry/Entity Type

Finance

Contact Information for Business Card

Name, address, email, title, services- money exchange and cross-border remittance

Requirements
Nice to have
• Digital age feel

```html
<!DOCTYPE html>
<html lang="en">
<head>
<meta charset="utf-8">
<title>Velorix Business Card</title>
<link rel="stylesheet" href="https://fonts.googleapis.com/css2?family=Montserrat:wght@400;500;600&display=swap">
<style>
  :root {
    --page: #e7e9eb;
    --card-dark: #303b46;
    --map-tone: #3c4955;
    --card-light: #f6f6f5;
    --ink: #2d3842;
    --ink-soft: #5a6570;
    --rule: #b9bec3;
    --accent: #5cc6d4;
    --accent-faint: rgba(92, 198, 212, 0.10);
    --white: #ffffff;
    --white-soft: #c9d3db;
  }
  * { box-sizing: border-box; margin: 0; padding: 0; }
  html, body { width: 1200px; height: 901px; overflow: hidden; }
  body {
    background: var(--page);
    font-family: "Montserrat", sans-serif;
    display: flex;
    flex-direction: column;
    align-items: center;
    justify-content: center;
    gap: 56px;
  }
  .card {
    width: 600px;
    height: 343px;
    position: relative;
    overflow: hidden;
    box-shadow: 0 10px 28px rgba(30, 40, 50, 0.18);
  }

  /* Back side */
  .card-back {
    background: var(--card-dark);
    display: flex;
    flex-direction: column;
    align-items: center;
    justify-content: center;
    gap: 22px;
  }
  .world-map {
    position: absolute;
    inset: 30px 20px;
    border-radius: 40%;
    background: radial-gradient(ellipse at center, var(--map-tone) 0%, rgba(60, 73, 85, 0.55) 45%, rgba(48, 59, 70, 0) 75%);
  }
  .tech-grid {
    position: absolute;
    inset: 0;
    background-image:
      linear-gradient(var(--accent-faint) 1px, transparent 1px),
      linear-gradient(90deg, var(--accent-faint) 1px, transparent 1px);
    background-size: 24px 24px;
    -webkit-mask-image: radial-gradient(ellipse at center, transparent 35%, #000 90%);
            mask-image: radial-gradient(ellipse at center, transparent 35%, #000 90%);
  }
  .data-line {
    position: absolute;
    left: 0; right: 0;
    bottom: 26px;
    height: 1px;
    background: linear-gradient(90deg, transparent, var(--accent) 50%, transparent);
    opacity: 0.6;
  }
  .brand {
    position: relative;
    display: flex;
    align-items: center;
    gap: 14px;
  }
  .brand-dot {
    width: 26px;
    height: 26px;
    border-radius: 50%;
    background: var(--accent);
  }
  .brand-name {
    font-weight: 600;
    letter-spacing: 2px;
    text-transform: uppercase;
  }
  .card-back .brand-name { color: var(--white); font-size: 40px; }
  .services {
    position: relative;
    font-size: 12px;
    font-weight: 500;
    letter-spacing: 2.5px;
    text-transform: uppercase;
    color: var(--white-soft);
  }
  .services .sep { color: var(--accent); margin: 0 10px; }

  /* Front side */
  .card-front { background: var(--card-light); }
  .accent-band {
    position: absolute;
    top: 0; left: 0; right: 0;
    height: 8px;
    background: var(--accent);
  }
  .card-front .brand {
    position: absolute;
    left: 44px;
    top: 62px;
    gap: 10px;
  }
  .card-front .brand-dot { width: 20px; height: 20px; }
  .card-front .brand-name { color: var(--ink); font-size: 28px; }
  .person {
    position: absolute;
    right: 44px;
    top: 58px;
  }
  .person-name {
    font-weight: 600;
    font-size: 22px;
    letter-spacing: 1.5px;
    color: var(--ink);
    text-transform: uppercase;
  }
  .person-title {
    font-size: 14px;
    color: var(--ink-soft);
    letter-spacing: 0.5px;
    margin-top: 2px;
  }
  .divider {
    position: absolute;
    left: 44px;
    right: 44px;
    top: 132px;
    height: 1px;
    background: var(--rule);
  }
  .contacts {
    position: absolute;
    left: 44px;
    top: 166px;
    list-style: none;
    display: flex;
    flex-direction: column;
    gap: 14px;
  }
  .contact {
    display: flex;
    align-items: flex-start;
    gap: 14px;
    font-size: 14px;
    color: var(--ink);
    letter-spacing: 0.3px;
    line-height: 1.3;
  }
  .contact svg { width: 16px; height: 16px; flex: none; margin-top: 1px; fill: var(--accent); }
  .front-services {
    position: absolute;
    right: 44px;
    bottom: 30px;
    font-size: 11px;
    font-weight: 500;
    letter-spacing: 1.5px;
    text-transform: uppercase;
    color: var(--ink-soft);
    text-align: right;
    line-height: 1.6;
  }
</style>
</head>
<body>

  <section class="card card-back" aria-label="Card back">
    <div class="world-map" role="img" aria-label="Faint world map in the background"></div>
    <div class="tech-grid" aria-hidden="true"></div>
    <div class="data-line" aria-hidden="true"></div>
    <div class="brand">
      <span class="brand-dot"></span>
      <span class="brand-name">Velorix</span>
    </div>
    <p class="services">Money Exchange<span class="sep">|</span>Cross-Border Remittance</p>
  </section>

  <section class="card card-front" aria-label="Card front">
    <div class="accent-band"></div>
    <div class="brand">
      <span class="brand-dot"></span>
      <span class="brand-name">Velorix</span>
    </div>
    <div class="person">
      <p class="person-name">Daniel Harrow</p>
      <p class="person-title">Managing Director</p>
    </div>
    <div class="divider"></div>
    <ul class="contacts">
      <li class="contact">
        <svg viewBox="0 0 24 24" aria-hidden="true"><path d="M6.6 10.8a15.2 15.2 0 0 0 6.6 6.6l2.2-2.2c.3-.3.7-.4 1-.2 1.1.4 2.3.6 3.6.6.6 0 1 .4 1 1V20c0 .6-.4 1-1 1A17 17 0 0 1 3 4c0-.6.4-1 1-1h3.5c.6 0 1 .4 1 1 0 1.3.2 2.5.6 3.6.1.3 0 .7-.2 1z"/></svg>
        <span>00198765432</span>
      </li>
      <li class="contact">
        <svg viewBox="0 0 24 24" aria-hidden="true"><path d="M2 5h20v14H2z M2 5l10 8 10-8" fill="none" stroke="var(--accent)" stroke-width="2.2" stroke-linejoin="round"/></svg>
        <span>daniel@velorix.com</span>
      </li>
      <li class="contact">
        <svg viewBox="0 0 24 24" aria-hidden="true"><path d="M12 2a7 7 0 0 0-7 7c0 5.2 7 13 7 13s7-7.8 7-13a7 7 0 0 0-7-7zm0 9.5A2.5 2.5 0 1 1 12 6.5a2.5 2.5 0 0 1 0 5z"/></svg>
        <span>Lorem ipsum dolor sit amet,<br>consectetur.</span>
      </li>
    </ul>
    <p class="front-services">Money Exchange<br>Cross-Border Remittance</p>
  </section>

</body>
</html>
```